CD-/Plattencover
Zielgruppe
Labelname: 'Kiesel & Fackel Label'; Produktion von Popmusik
Aufgabenstellung
Die Texte der Songs gehen massiv in die Tiefe und werden freundlich und sanft vorgebracht. Die Musik hat einen leichten Countryblues-Touch.
Ich brauche auf der Rückseite der EP sämtliche Spezifikationen, die auf einer CD verlangt werden.
Der Titel lautet 'Morgenrot, Tauwind' und bezieht sich auf die Kürze des Lebens. Die Grundstimmung der Musik ist dennoch fröhlich (ironisch).

```html
<!DOCTYPE html>
<html lang="de">
<head>
<meta charset="utf-8">
<title>Morgenrot, Tauwind – Kiesel &amp; Fackel Label</title>
<link rel="stylesheet" href="https://fonts.googleapis.com/css2?family=Bodoni+Moda:wght@400;800&display=swap">
<style>
  :root {
    --backdrop: #e6e6e6;
    --sky-light: #f6efe8;
    --sky-warm: #f0c8a4;
    --field-glow: #c85a2c;
    --field-mid: #8a2c17;
    --field-deep: #3a120c;
    --label-orange: #ea6a1e;
    --label-red: #e1352c;
    --title-white: #ffffff;
  }
  html, body {
    margin: 0;
    padding: 0;
    width: 1200px;
    height: 907px;
    overflow: hidden;
    background: var(--backdrop);
  }
  .cover {
    position: absolute;
    left: 170px;
    top: 23px;
    width: 860px;
    height: 860px;
    overflow: hidden;
  }
  .cover-photo {
    position: absolute;
    inset: 0;
    width: 100%;
    height: 100%;
    display: block;
  }
  .label-name {
    position: absolute;
    left: 70px;
    top: 120px;
    display: flex;
    align-items: center;
    gap: 14px;
    font-family: "Bodoni Moda", "Didot", serif;
    font-weight: 800;
    font-size: 40px;
    line-height: 1;
    color: var(--label-orange);
    letter-spacing: 0.5px;
  }
  .label-dot {
    width: 30px;
    height: 30px;
    border-radius: 50%;
    background: var(--label-red);
    flex: none;
  }
  .album-title {
    position: absolute;
    left: 0;
    right: 0;
    bottom: 48px;
    padding-left: 110px;
    text-align: center;
    font-family: "Bodoni Moda", "Didot", serif;
    font-weight: 400;
    font-size: 38px;
    letter-spacing: 1px;
    color: var(--title-white);
  }
</style>
</head>
<body>
  <main class="cover">
    <svg class="cover-photo" viewBox="0 0 860 860" preserveAspectRatio="none"
         role="img" aria-label="Foto: Mädchen im Sommerkleid dreht sich im Gegenlicht der Abendsonne auf einer Wiese mit hohem Gras und Büschen">
      <defs>
        <linearGradient id="meadow" x1="0" y1="0" x2="0" y2="1">
          <stop offset="0" stop-color="var(--sky-light)"/>
          <stop offset="0.3" stop-color="var(--sky-warm)"/>
          <stop offset="0.42" stop-color="var(--field-glow)"/>
          <stop offset="0.65" stop-color="var(--field-mid)"/>
          <stop offset="1" stop-color="var(--field-deep)"/>
        </linearGradient>
        <radialGradient id="sun" cx="0.85" cy="0.2" r="0.55">
          <stop offset="0" stop-color="#ffffff" stop-opacity="0.9"/>
          <stop offset="1" stop-color="#ffffff" stop-opacity="0"/>
        </radialGradient>
      </defs>
      <rect width="860" height="860" fill="url(#meadow)"/>
      <rect width="860" height="860" fill="url(#sun)"/>
    </svg>

    <div class="label-name">
      <span class="label-dot"></span>
      <span>Kiesel &amp; Fackel Label</span>
    </div>

    <h1 class="album-title" style="margin:0">Morgenrot, Tauwind</h1>
  </main>
</body>
</html>
```